Start up in business consultancy needs a business card

We need the business card's layout (we have already the logo). Our business is concerned on consultancy services delivered to companies on the matter of sustainability. Business card should be enough essentials and professional style.

Side A with the following info:
logo + a space for the claim (still to identify) + website of the company

Side B with the following info:
Name of business card holder + title of the business card holder + address of the company + space for mobile number, phone number, fax number + e-mail of business card holder + graphic details around.

Target Market(s)

Business of any sector

Industry/Entity Type

Business Service

Contact Information for Business Card

Name of the company:
Pianoverde srl
Società Benefit

Address of the company:
Via Lucerna, 7
21047 - Saronno (VA)

Website:
www.pianoverde.it

Name of the BC' holder:
Luca Ferentino

Title:
Co-fondatore

Email:
luca@pianoverde.it

Mobile:
+39 348 915 2074
Phone:
+39 348 915 2074
Fax:
+39 348 915 2074

Font styles to use
Other font styles liked:
• new gothic

```html
<!DOCTYPE html>
<html lang="it">
<head>
<meta charset="utf-8">
<title>Pianoverde – biglietti da visita</title>
<link rel="stylesheet" href="https://fonts.googleapis.com/css2?family=Source+Sans+3:wght@400;600&display=swap">
<style>
  :root {
    --brand-blue: #0565a8;
    --ink: #4a4a4a;
    --paper: #ffffff;
    --stage: #e9e7e4;
    --rule: #c9c9c9;
    --divider: #d8d8d8;
    --ghost: rgba(255,255,255,0.14);
  }
  html, body {
    margin: 0;
    width: 1200px;
    height: 802px;
    overflow: hidden;
    background: var(--stage);
    font-family: "Source Sans 3", "Myriad Pro", sans-serif;
  }
  .stage { position: relative; width: 1200px; height: 802px; }
  .card {
    position: absolute;
    width: 499px;
    height: 285px;
    border-radius: 16px;
    overflow: hidden;
  }
  .card--blue { background: var(--brand-blue); color: var(--paper); }
  .card--white { background: var(--paper); color: var(--ink); }
  .card--info { left: 87px; top: 106px; }
  .card--emblem { left: 614px; top: 106px; }
  .card--ghost { left: 87px; top: 411px; }
  .card--ring { left: 614px; top: 411px; }

  /* info side */
  .mark-circle {
    position: absolute; left: 45px; top: 110px;
    width: 58px; height: 58px; border: 3px solid var(--brand-blue); border-radius: 50%;
  }
  .info-wordmark {
    position: absolute; left: 118px; top: 126px;
    font-size: 22px; color: var(--brand-blue); font-weight: 400; line-height: 1;
  }
  .divider { position: absolute; left: 276px; top: 42px; width: 1px; height: 204px; background: var(--divider); }
  .holder { position: absolute; left: 297px; top: 39px; line-height: 1.15; }
  .holder__name { font-size: 20px; color: var(--brand-blue); }
  .holder__name strong { font-weight: 600; }
  .holder__title { font-size: 16px; color: var(--ink); }
  .company { position: absolute; left: 297px; top: 90px; font-size: 13.5px; line-height: 18px; color: var(--ink); }
  .contacts { position: absolute; left: 297px; top: 168px; list-style: none; margin: 0; padding: 0; font-size: 13.5px; color: var(--ink); }
  .contacts li { display: flex; align-items: center; height: 19px; }
  .contacts svg { width: 13px; height: 13px; margin-right: 7px; fill: var(--brand-blue); }
  .footer-rule { position: absolute; left: 0; right: 0; top: 271px; height: 1px; background: var(--rule); }
  .footer-band { position: absolute; left: 0; right: 0; top: 273px; height: 12px; background: var(--brand-blue); }

  /* emblem side */
  .emblem-circle {
    position: absolute; left: 171px; top: 55px; width: 150px; height: 150px;
    border: 5px solid var(--paper); border-radius: 50%;
    display: flex; align-items: center; justify-content: center;
  }
  .emblem-name { font-size: 26px; font-weight: 600; color: var(--paper); }
  .site { font-size: 13px; letter-spacing: 3px; color: var(--paper); line-height: 1; }
  .card--emblem .site { position: absolute; left: 0; right: 0; top: 240px; text-align: center; }

  /* back sides */
  .big-circle { position: absolute; left: 14px; top: 13px; width: 254px; height: 254px; border-radius: 50%; }
  .big-circle--ghost { border: 6px solid var(--ghost); }
  .big-circle--solid { border: 6px solid var(--paper); }
  .back-wordmark { position: absolute; right: 32px; top: 216px; font-size: 31px; font-weight: 400; line-height: 1; color: var(--paper); }
  .card--ghost .site, .card--ring .site { position: absolute; right: 32px; top: 250px; }
</style>
</head>
<body>
<main class="stage">

  <section class="card card--white card--info">
    <div class="mark-circle"></div>
    <div class="info-wordmark">pianoverde</div>
    <div class="divider"></div>
    <div class="holder">
      <div class="holder__name">Luca <strong>Ferentino</strong></div>
      <div class="holder__title">Co-fondatore</div>
    </div>
    <div class="company">
      Pianoverde srl<br>Società Benefit<br>Via Lucerna, 7<br>21047 - Saronno (VA)
    </div>
    <ul class="contacts">
      <li><svg viewBox="0 0 16 16"><path d="M3.5 1l3 3-1.6 1.8a9 9 0 0 0 5.3 5.3L12 9.5l3 3-2 2C6.5 14 2 9.5 1.5 3z"/></svg>+39 348 915 2074</li>
      <li><svg viewBox="0 0 16 16"><path d="M4 0h8a1 1 0 0 1 1 1v14a1 1 0 0 1-1 1H4a1 1 0 0 1-1-1V1a1 1 0 0 1 1-1zm1 2v10h6V2zm3 11a1 1 0 1 0 0 2 1 1 0 0 0 0-2z"/></svg>+39 348 915 2074</li>
      <li><svg viewBox="0 0 16 16"><path d="M4 1h8v4H4zM1 6h14v7h-2v2H3v-2H1zm4 4v3h6v-3z"/></svg>+39 348 915 2074</li>
      <li><svg viewBox="0 0 16 16"><path d="M1 3h14v1L8 9 1 4zm0 3l7 5 7-5v7H1z"/></svg>luca@pianoverde.it</li>
    </ul>
    <div class="footer-rule"></div>
    <div class="footer-band"></div>
  </section>

  <section class="card card--blue card--emblem">
    <div class="emblem-circle"><span class="emblem-name">pianoverde</span></div>
    <div class="site">www.pianoverde.it</div>
  </section>

  <section class="card card--blue card--ghost">
    <div class="big-circle big-circle--ghost"></div>
    <div class="back-wordmark">pianoverde</div>
    <div class="site">www.pianoverde.it</div>
  </section>

  <section class="card card--blue card--ring">
    <div class="big-circle big-circle--solid"></div>
    <div class="back-wordmark">pianoverde</div>
    <div class="site">www.pianoverde.it</div>
  </section>

</main>
</body>
</html>
```